Copperfen Hollow Wine And Spirits

We need to design a website for our Liquor Store

Industry/Entity Type

Store

Number of Pages Required

4 page

Requirements
Must have
• Beer, Liquor, Wine & Cigar related theme.
• Mention our 8-locations addresses & maps info
Nice to have
• category for Beer, Liquor & Wine to setup database for item list to link our sql server database.

```html
<!DOCTYPE html>
<html lang="en">
<head>
<meta charset="utf-8">
<title>Copperfen Hollow Wine And Spirits</title>
<link href="https://fonts.googleapis.com/css2?family=Roboto:wght@300;400;500;700&family=Great+Vibes&display=swap" rel="stylesheet">
<style>
:root{
  --red:#d1202f;
  --red-dark:#b5141f;
  --ink:#333333;
  --muted:#8a8a8a;
  --white:#ffffff;
  --black:#0b0b0b;
  --line:#e2e2e2;
  --amber:#c98a2c;
  --wood:#4a2a12;
}
*{box-sizing:border-box;margin:0;padding:0}
html,body{width:1200px;height:3327px;overflow:hidden}
body{position:relative;font-family:"Roboto",Arial,sans-serif;color:var(--ink);background:var(--white)}
.abs{position:absolute}
.script{font-family:"Great Vibes",cursive;font-weight:400;color:#444}
.section-title{position:absolute;font-size:40px;text-align:center}
.section-title::after{content:"";display:block;width:90px;height:1px;background:#bbb;margin:6px auto 0}
.btn{position:absolute;background:var(--red);color:var(--white);font-size:13px;font-weight:500;text-transform:uppercase;border-radius:6px;display:flex;align-items:center;justify-content:center;letter-spacing:.3px}

/* hero */
.hero{left:0;top:0;width:1200px;height:517px;background:radial-gradient(ellipse at 25% 55%,#e9b04a 0%,#a8651c 35%,#3f2410 70%,#1c120b 100%)}
.hero-circle{left:391px;top:54px;width:380px;height:380px;border-radius:50%;background:rgba(255,255,255,.82)}
.brand{left:472px;top:62px;width:253px;height:112px;display:flex;align-items:center;gap:10px;justify-content:center;font-size:21px;font-weight:700;color:var(--red);line-height:1.15;text-align:left}
.brand .mark{width:22px;height:22px;border-radius:50%;background:var(--red);flex:none}
.hero-title{left:400px;top:205px;width:362px;text-align:center;color:var(--red);font-size:38px;font-weight:400}
.hero-text{left:465px;top:264px;width:232px;text-align:center;font-size:15px;line-height:20px;color:#222}

/* menu */
.menu{left:858px;top:0;width:342px;height:3327px;background:rgba(0,0,0,.72);z-index:10}
.menu-close{left:22px;top:14px;width:40px;height:40px}
.menu ul{list-style:none;position:absolute;left:30px;top:74px}
.menu li{color:var(--white);font-size:31px;font-weight:400;height:94.5px;line-height:44px}

/* about */
.about-title{left:236px;top:598px;width:300px}
.about-text{left:137px;top:678px;width:498px;text-align:center;font-size:13px;line-height:20px;color:var(--muted)}

/* tabs */
.tabs{left:0;top:905px;width:1200px;height:67px;background:var(--red);display:flex;justify-content:center;align-items:center}
.tabs span{color:var(--white);font-size:16px;font-weight:500;padding:0 44px;border-right:1px solid rgba(255,255,255,.6);line-height:40px}
.tabs span:last-child{border-right:none}
.tabs .inner{position:absolute;left:414px;display:flex}

/* photo strip */
.strip-a{left:0;top:972px;width:404px;height:304px;background:linear-gradient(135deg,#5a3414 0%,#c98a2c 50%,#2b1a0d 100%)}
.strip-b{left:404px;top:972px;width:401px;height:304px;background:linear-gradient(160deg,#d9525a 0%,#c8303a 55%,#9e1c26 100%)}
.strip-c{left:805px;top:972px;width:395px;height:304px;background:linear-gradient(135deg,#3a2410 0%,#b87a2a 60%,#2a1a0d 100%)}
.strip-b p{position:absolute;left:0;top:108px;width:401px;text-align:center;color:var(--white);font-size:33px;font-weight:300}

/* category */
.cat-title{left:450px;top:1325px;width:300px}
.cat-col{top:1420px;width:317px}
.cat-col h3{text-align:center;font-size:20px;font-weight:400;color:#444;margin-bottom:20px}
.price-row{display:flex;font-size:13px;line-height:21px;color:#444}
.price-row .leader{flex:1;border-bottom:1px dotted #555;margin:0 2px 6px}

/* blog */
.blog-bg{left:0;top:1708px;width:1200px;height:521px;background:linear-gradient(180deg,#2a1a10 0%,#4b2e17 50%,#1b120b 100%)}
.blog-photo{left:244px;top:1752px;width:339px;height:433px;background:radial-gradient(ellipse at 50% 60%,#e4a23c 0%,#7a4616 45%,#23160c 100%);border:2px solid #bba88f}
.blog-panel{left:583px;top:1752px;width:371px;height:433px;background:var(--white)}
.blog-title{left:110px;top:18px;width:200px;font-size:38px}
.post{position:absolute;left:0;width:371px;height:85px;display:flex;align-items:center;padding-left:20px}
.post.active{background:var(--red)}
.date{width:58px;height:64px;background:var(--red);color:var(--white);text-align:center;border:2px solid var(--white);flex:none;display:flex;flex-direction:column;justify-content:center}
.date b{font-size:26px;font-weight:500;line-height:28px}
.date small{font-size:10px}
.year{width:14px;font-size:12px;color:var(--red);line-height:14px;text-align:center;margin:0 6px 0 2px}
.post.active .year{color:var(--white)}
.post h4{font-size:15px;font-weight:400;color:var(--red);margin-bottom:4px}
.post p{font-size:12px;line-height:17px;color:#666}
.post.active h4,.post.active p{color:var(--white)}

/* services */
.svc-title{left:450px;top:2287px;width:300px}
.svc{top:2388px;width:300px;text-align:center}
.svc .ring{width:72px;height:72px;margin:0 auto}
.svc h4{font-size:16px;font-weight:400;color:#444;margin-top:26px}
.svc p{font-size:13px;line-height:18px;color:var(--muted);margin:6px auto 0;width:230px}

/* locations */
.loc-bg{left:0;top:2628px;width:1200px;height:470px;background:linear-gradient(180deg,#2b1b10 0%,#4a2d17 60%,#1e140c 100%)}
.map{left:98px;top:2673px;width:445px;height:383px;background:linear-gradient(135deg,#e6e6e2 0%,#d6d8d4 50%,#e9e7e1 100%)}
.loc-panel{left:543px;top:2673px;width:559px;height:383px;background:var(--white)}
.loc-title{left:168px;top:8px;width:260px;font-size:34px}
.loc-card{position:absolute;left:56px;width:417px;height:86px;border:1px solid var(--line);border-radius:4px;display:flex;padding:12px 16px;font-size:11px;line-height:15px;color:#444;background:var(--white)}
.loc-card.active{background:var(--red);color:var(--white);border-color:var(--red)}
.loc-card.active::before{content:"";position:absolute;left:-14px;top:22px;border:7px solid transparent;border-right-color:var(--red)}
.loc-card .l{width:220px}
.loc-card .r{flex:1}
.loc-card .item{display:flex;gap:8px;margin-bottom:6px}
.loc-card svg{flex:none;margin-top:2px}

/* footer */
.footer{left:0;top:3098px;width:1200px;height:229px;background:var(--black);color:var(--white)}
.fcol{position:absolute;top:18px;font-size:13px;line-height:20px}
.fcol h5{font-size:14px;font-weight:500;margin-bottom:12px}
.fcol p{color:#ddd}
.fcol li{list-style:none;color:#ddd;line-height:25px}
.copyright{position:absolute;left:0;top:3292px;width:1200px;text-align:center;font-size:12px;color:#ddd;border-top:1px solid #333;padding-top:6px}
</style>
</head>
<body>

<header class="abs hero" role="img" aria-label="Photo of beer glasses and a wooden barrel in a warm-lit bar"></header>
<div class="abs hero-circle"></div>
<div class="abs brand"><span class="mark"></span><span>Copperfen Hollow<br>Wine &amp; Spirits</span></div>
<h1 class="abs hero-title">LOREM IPSUM IS</h1>
<p class="abs hero-text">Lorem Ipsum is simply dummy text of the printing and typesetting industry. Lorem Ipsum has been the industry's standard dummy text ever since the.</p>
<a class="btn" style="left:532px;top:384px;width:133px;height:35px">Read more</a>

<section>
  <h2 class="section-title script about-title">About Us</h2>
  <p class="abs about-text">Lorem Ipsum is simply dummy text of the printing and typesetting industry. Lorem Ipsum has been the industry's standard dummy text ever since the 1500s, when an unknown printer took a galley of type and scrambled it to make a type specimen book. It has survived not only five centuries.</p>
  <a class="btn" style="left:320px;top:785px;width:133px;height:30px">Read more</a>
</section>

<nav class="abs tabs"><div class="inner"><span>Beer</span><span>Liquor</span><span>Wine</span></div></nav>

<div class="abs strip-a" role="img" aria-label="Photo of beer bottles and glasses beside a barrel"></div>
<div class="abs strip-b" role="img" aria-label="Photo of a bar interior under a red tint">
  <p>Lorem Ipsum is simply</p>
  <svg class="abs" style="left:186px;top:162px" width="30" height="30" viewBox="0 0 30 30"><circle cx="12" cy="12" r="8" fill="none" stroke="#fff" stroke-width="4"/><line x1="18" y1="18" x2="27" y2="27" stroke="#fff" stroke-width="5" stroke-linecap="round"/></svg>
</div>
<div class="abs strip-c" role="img" aria-label="Photo of beer on a bar counter"></div>

<section>
  <h2 class="section-title script cat-title">Category</h2>
  <div class="abs cat-col" style="left:100px">
    <h3>Wine</h3>
    <div class="price-row"><span>Lorem Ipsum is simply dummy</span><span class="leader"></span><span>$ 5235.00</span></div>
    <div class="price-row"><span>Orem Ipsum is simply dummy</span><span class="leader"></span><span>$ 8235.00</span></div>
    <div class="price-row"><span>Rem Ipsum is dummy</span><span class="leader"></span><span>$ 9235.00</span></div>
    <div class="price-row"><span>psum is simply dummy</span><span class="leader"></span><span>$ 2235.00</span></div>
    <div class="price-row"><span>Orem Ipsum is simply dummy</span><span class="leader"></span><span>$ 4235.00</span></div>
    <div class="price-row"><span>Rem Ipsum is dummy</span><span class="leader"></span><span>$ 3235.00</span></div>
  </div>
  <div class="abs cat-col" style="left:441px">
    <h3>Beer</h3>
    <div class="price-row"><span>Ipsum is simply dummy</span><span class="leader"></span><span>$ 235.00</span></div>
    <div class="price-row"><span>Orem Ipsum is simply dummy</span><span class="leader"></span><span>$ 1235.00</span></div>
    <div class="price-row"><span>Rem Ipsum is dummy</span><span class="leader"></span><span>$ 1035.00</span></div>
    <div class="price-row"><span>psum is simply dummy</span><span class="leader"></span><span>$ 4235.00</span></div>
    <div class="price-row"><span>Orem Ipsum is simply dummy</span><span class="leader"></span><span>$ 8235.00</span></div>
    <div class="price-row"><span>Rem Ipsum is dummy</span><span class="leader"></span><span>$ 9235.00</span></div>
  </div>
  <div class="abs cat-col" style="left:783px">
    <h3>Liquore</h3>
    <div class="price-row"><span>Ipsum is simply dummy</span><span class="leader"></span><span>$ 5235.00</span></div>
    <div class="price-row"><span>Orem Ipsum is simply dummy</span><span class="leader"></span><span>$ 8235.00</span></div>
    <div class="price-row"><span>Rem Ipsum is dummy</span><span class="leader"></span><span>$ 1235.00</span></div>
    <div class="price-row"><span>psum is simply dummy</span><span class="leader"></span><span>$ 3235.00</span></div>
    <div class="price-row"><span>Orem Ipsum is simply dummy</span><span class="leader"></span><span>$ 6235.00</span></div>
    <div class="price-row"><span>Rem Ipsum is dummy</span><span class="leader"></span><span>$ 8235.00</span></div>
  </div>
  <a class="btn" style="left:192px;top:1612px;width:133px;height:29px">View more</a>
  <a class="btn" style="left:534px;top:1612px;width:133px;height:29px">View more</a>
  <a class="btn" style="left:876px;top:1612px;width:133px;height:29px">View more</a>
</section>

<section>
  <div class="abs blog-bg" role="img" aria-label="Blurred photo of a dim bar interior"></div>
  <div class="abs blog-photo" role="img" aria-label="Photo of a pint of beer on a bar counter"></div>
  <div class="abs blog-panel">
    <h2 class="section-title script blog-title">Our Blog</h2>
    <article class="post active" style="top:93px">
      <div class="date"><b>22</b><small>January</small></div><div class="year">2<br>0<br>1<br>7</div>
      <div><h4>Lorem Ipsum is simply</h4><p>Lorem Ipsum is simply dummy text of the print-<br>ing and typesetting industry.</p></div>
    </article>
    <article class="post" style="top:200px">
      <div class="date"><b>22</b><small>January</small></div><div class="year">2<br>0<br>1<br>7</div>
      <div><h4>Lorem Ipsum is simply</h4><p>Lorem Ipsum is simply dummy text of the print-<br>ing and typesetting industry.</p></div>
    </article>
    <article class="post" style="top:312px">
      <div class="date"><b>22</b><small>January</small></div><div class="year">2<br>0<br>1<br>7</div>
      <div><h4>Lorem Ipsum is simply</h4><p>Lorem Ipsum is simply dummy text of the print-<br>ing and typesetting industry.</p></div>
    </article>
  </div>
</section>

<section>
  <h2 class="section-title script svc-title">Our Services</h2>
  <div class="abs svc" style="left:107px">
    <svg class="ring" viewBox="0 0 72 72"><circle cx="36" cy="36" r="33" fill="none" stroke="var(--red)" stroke-width="3"/><circle cx="36" cy="36" r="26" fill="none" stroke="#f2b8bd" stroke-width="2"/><rect x="22" y="30" width="28" height="18" rx="2" fill="var(--red)"/><rect x="26" y="22" width="20" height="6" fill="var(--red)"/></svg>
    <h4>Is simply dummy</h4>
    <p>Lorem Ipsum is simply dummy text of the printing and typesetting industry.</p>
  </div>
  <div class="abs svc" style="left:449px">
    <svg class="ring" viewBox="0 0 72 72"><circle cx="36" cy="36" r="33" fill="none" stroke="var(--red)" stroke-width="3"/><circle cx="36" cy="36" r="26" fill="none" stroke="#f2b8bd" stroke-width="2"/><rect x="30" y="20" width="12" height="30" rx="2" fill="var(--red)"/><rect x="26" y="46" width="20" height="6" fill="var(--red)"/></svg>
    <h4>Is simply dummy</h4>
    <p>Lorem Ipsum is simply dummy text of the printing and typesetting industry.</p>
  </div>
  <div class="abs svc" style="left:793px">
    <svg class="ring" viewBox="0 0 72 72"><circle cx="36" cy="36" r="33" fill="none" stroke="var(--red)" stroke-width="3"/><circle cx="36" cy="36" r="26" fill="none" stroke="#f2b8bd" stroke-width="2"/><rect x="22" y="24" width="28" height="24" rx="2" fill="none" stroke="var(--red)" stroke-width="3"/></svg>
    <h4>Is simply dummy</h4>
    <p>Lorem Ipsum is simply dummy text of the printing and typesetting industry.</p>
  </div>
</section>

<section>
  <div class="abs loc-bg" role="img" aria-label="Blurred photo of a bar at night"></div>
  <div class="abs map" role="img" aria-label="Street map showing the store locations"></div>
  <div class="abs loc-panel">
    <h2 class="section-title script loc-title">Our Locations</h2>
    <div class="loc-card active" style="top:68px">
      <div class="l">
        <div class="item"><svg width="10" height="10" viewBox="0 0 10 10"><path d="M2 0h2l1 3-1.5 1a6 6 0 0 0 2.5 2.5L7 5l3 1v2a2 2 0 0 1-2 2A8 8 0 0 1 0 2a2 2 0 0 1 2-2z" fill="currentColor"/></svg>000 - 0000 - 00000</div>
        <div class="item"><svg width="10" height="10" viewBox="0 0 10 10"><path d="M5 0 0 5h1.5v5h7V5H10z" fill="currentColor"/></svg>Lorem Ipsum is simply and typesetting industry. the industry's standard</div>
      </div>
      <div class="r">
        <div class="item"><svg width="10" height="10" viewBox="0 0 10 10"><rect y="1" width="10" height="8" fill="currentColor"/></svg>info@copperfenhollow.com</div>
        <div class="item"><svg width="10" height="10" viewBox="0 0 10 10"><circle cx="5" cy="5" r="4" fill="none" stroke="currentColor" stroke-width="1.5"/></svg>Monday - Saturday 10.00 am - 10.00 pm Sunday - Closed</div>
      </div>
    </div>
    <div class="loc-card" style="top:173px">
      <div class="l">
        <div class="item"><svg width="10" height="10" viewBox="0 0 10 10"><path d="M2 0h2l1 3-1.5 1a6 6 0 0 0 2.5 2.5L7 5l3 1v2a2 2 0 0 1-2 2A8 8 0 0 1 0 2a2 2 0 0 1 2-2z" fill="currentColor"/></svg>000 - 0000 - 00000</div>
        <div class="item"><svg width="10" height="10" viewBox="0 0 10 10"><path d="M5 0 0 5h1.5v5h7V5H10z" fill="currentColor"/></svg>Lorem Ipsum is simply and typesetting industry. the industry's standard</div>
      </div>
      <div class="r">
        <div class="item"><svg width="10" height="10" viewBox="0 0 10 10"><rect y="1" width="10" height="8" fill="currentColor"/></svg>info@copperfenhollow.com</div>
        <div class="item"><svg width="10" height="10" viewBox="0 0 10 10"><circle cx="5" cy="5" r="4" fill="none" stroke="currentColor" stroke-width="1.5"/></svg>Monday - Saturday 10.00 am - 10.00 pm Sunday - Closed</div>
      </div>
    </div>
    <div class="loc-card" style="top:277px">
      <div class="l">
        <div class="item"><svg width="10" height="10" viewBox="0 0 10 10"><path d="M2 0h2l1 3-1.5 1a6 6 0 0 0 2.5 2.5L7 5l3 1v2a2 2 0 0 1-2 2A8 8 0 0 1 0 2a2 2 0 0 1 2-2z" fill="currentColor"/></svg>000 - 0000 - 00000</div>
        <div class="item"><svg width="10" height="10" viewBox="0 0 10 10"><path d="M5 0 0 5h1.5v5h7V5H10z" fill="currentColor"/></svg>Lorem Ipsum is simply and typesetting industry. the industry's standard</div>
      </div>
      <div class="r">
        <div class="item"><svg width="10" height="10" viewBox="0 0 10 10"><rect y="1" width="10" height="8" fill="currentColor"/></svg>info@copperfenhollow.com</div>
        <div class="item"><svg width="10" height="10" viewBox="0 0 10 10"><circle cx="5" cy="5" r="4" fill="none" stroke="currentColor" stroke-width="1.5"/></svg>Monday - Saturday 10.00 am - 10.00 pm Sunday - Closed</div>
      </div>
    </div>
  </div>
</section>

<footer class="abs footer">
  <div class="fcol" style="left:100px;width:290px">
    <h5>About Us</h5>
    <p>Lorem Ipsum is simply dummy text of the printing and typesetting industry. Lorem Ipsum has been the industry's standard dummy text ever since the 1500s, when an unknown printer took a galley of type and scrambled it make a type specimen book.</p>
  </div>
  <div class="fcol" style="left:501px;width:210px">
    <h5>Recent News</h5>
    <p>Ipsum is simply dummy text of the printing and typesetting<br>12/08/2017</p>
    <p style="margin-top:12px">Ipsum is simply dummy text of the printing and typesetting<br>12/08/2017</p>
  </div>
  <div class="fcol" style="left:843px">
    <h5>Quick Links</h5>
    <ul><li>Home</li><li>About Us</li><li>Category</li><li>Our Blog</li><li>Contact Us</li></ul>
  </div>
  <div class="fcol" style="left:1036px">
    <h5>Category</h5>
    <ul><li>Wine</li><li>Beer</li><li>Liquore</li></ul>
  </div>
</footer>
<p class="copyright">copperfenhollow.com © 2015-2017 All rights reserved. Privacy policy</p>

<nav class="abs menu">
  <svg class="abs menu-close" viewBox="0 0 40 40"><circle cx="20" cy="20" r="18" fill="none" stroke="#fff" stroke-width="2"/><path d="M13 13l14 14M27 13 13 27" stroke="#fff" stroke-width="2.5"/></svg>
  <ul><li>Home</li><li>About Us</li><li>Category</li><li>Our Blog</li><li>Contact Us</li></ul>
</nav>

</body>
</html>
```